Business Card Design

Buy and sell properties
Buy and rehab properties
Buy properties for cash
That is what I do but do need a logo
looking for some type of logo or design on it
Just started business
Back of card should say something like BUY HOUSES CASH
Overview: it is a new company. Basically I buy properties wholesale and fix them up and sell them or sell them to other fix and flippers
Background: company is new so not any background
Market: is basically anyone selling a house or buying a house. Someone that needs to sell house fast. Basically I am a cash home buyer!!!

Updates
Email on card should be:   harborlanerealtyinc@mailbox.test

Industry/Entity Type
House
Contact Information for Business Card
Harbor Lane Realty Inc
PO Box 718269
Cedar Marsh FL 32987

Dale Morrick
dmorrick@mailbox.test
555-271-6094

```html
<!DOCTYPE html>
<html lang="en">
<head>
<meta charset="utf-8">
<title>Harbor Lane Realty Inc — Business Card</title>
<link href="https://fonts.googleapis.com/css2?family=Arimo:wght@400;700&family=Marcellus&display=swap" rel="stylesheet">
<style>
  :root {
    --bg-light: #e9e9e9;
    --bg-dark: #a9a9a9;
    --brand-green: #2f7d1f;
    --deep-green: #1f5e14;
    --lime: #8fb43a;
    --card-black: #0c0c0c;
    --card-grey: #4a4a4a;
    --text-light: #e6e6e6;
    --text-muted: #c9c9c9;
    --icon-fill: #d9d9d9;
  }
  * { box-sizing: border-box; margin: 0; padding: 0; }
  html, body { width: 1200px; height: 1200px; overflow: hidden; }
  body {
    position: relative;
    background: linear-gradient(135deg, var(--bg-light) 0%, #d3d3d3 45%, var(--bg-dark) 100%);
    font-family: "Arimo", Arial, sans-serif;
  }

  .brand-lockup {
    position: absolute;
    left: 40px; top: 110px;
    display: flex; align-items: center; gap: 18px;
  }
  .brand-lockup .brand-dot {
    width: 34px; height: 34px; border-radius: 50%;
    background: var(--brand-green);
  }
  .brand-lockup .brand-name {
    font-weight: 700; font-size: 46px;
    color: var(--deep-green);
    letter-spacing: 0.5px;
  }

  .card {
    position: absolute;
    width: 700px; height: 400px;
    overflow: hidden;
    box-shadow: 0 10px 28px rgba(0,0,0,0.35);
  }
  .card-bg { position: absolute; inset: 0; width: 100%; height: 100%; }

  /* Front */
  .card-front { left: 40px; top: 300px; }
  .card-front .front-brand {
    position: absolute; left: 40px; top: 150px; width: 310px;
    display: flex; align-items: center; gap: 10px;
  }
  .front-brand .brand-dot { width: 16px; height: 16px; border-radius: 50%; background: var(--lime); flex: none; }
  .front-brand .brand-name {
    font-weight: 700; font-size: 24px; color: var(--text-light); white-space: nowrap;
  }
  .card-front .divider {
    position: absolute; left: 372px; top: 38px;
    width: 2px; height: 200px;
    background: linear-gradient(180deg, rgba(255,255,255,0) 0%, #d6d6d6 50%, rgba(255,255,255,0) 100%);
  }
  .card-front .holder {
    position: absolute; left: 380px; top: 26px; width: 290px; text-align: right;
  }
  .holder .holder-name {
    font-family: "Marcellus", Georgia, serif;
    font-weight: 400;
    font-size: 34px; line-height: 1.1;
    color: var(--text-light); letter-spacing: 1.5px;
    text-transform: uppercase; white-space: nowrap;
  }
  .holder .holder-title {
    font-family: "Marcellus", Georgia, serif;
    font-size: 16px; line-height: 1.3; color: var(--text-muted);
    margin-top: 2px; padding-right: 30px; white-space: nowrap;
  }
  .contact-list {
    position: absolute; left: 392px; top: 108px;
    list-style: none;
  }
  .contact-list li {
    display: flex; align-items: center; gap: 14px;
    height: 34px;
    font-size: 19px; color: var(--text-light); white-space: nowrap;
  }
  .contact-list .icon {
    width: 26px; height: 26px; border-radius: 6px;
    background: var(--icon-fill);
    display: flex; align-items: center; justify-content: center; flex: none;
  }
  .contact-list .icon svg { width: 18px; height: 18px; }

  /* Back */
  .card-back { left: 460px; top: 760px; }
  .card-back .back-brand {
    position: absolute; left: 0; right: 0; top: 140px;
    display: flex; justify-content: center; align-items: center; gap: 12px;
  }
  .back-brand .brand-dot { width: 18px; height: 18px; border-radius: 50%; background: var(--lime); }
  .back-brand .brand-name { font-weight: 700; font-size: 28px; color: var(--text-light); white-space: nowrap; }
  .card-back .tagline {
    position: absolute; left: 0; right: 0; top: 300px; text-align: center;
    font-family: "Marcellus", Georgia, serif;
    font-size: 33px; color: var(--text-light); letter-spacing: 1px;
  }
  .card-back .tagline-rule {
    position: absolute; left: 240px; width: 220px; top: 348px; height: 3px;
    background: linear-gradient(90deg, rgba(143,180,58,0) 0%, var(--lime) 50%, rgba(143,180,58,0) 100%);
  }
</style>
</head>
<body>

  <header class="brand-lockup">
    <span class="brand-dot"></span>
    <span class="brand-name">Harbor Lane Realty Inc</span>
  </header>

  <section class="card card-front" aria-label="Business card front">
    <svg class="card-bg" viewBox="0 0 700 400" preserveAspectRatio="none" aria-hidden="true">
      <defs>
        <radialGradient id="frontGlow" cx="0.38" cy="0.4" r="0.6">
          <stop offset="0" stop-color="#4a4a4a"/>
          <stop offset="1" stop-color="#0c0c0c"/>
        </radialGradient>
      </defs>
      <rect width="700" height="400" fill="url(#frontGlow)"/>
      <path d="M0 310 C 300 340, 600 310, 700 250 L700 400 L0 400 Z" fill="#8fb43a"/>
      <path d="M0 324 C 300 354, 610 324, 700 268 L700 400 L0 400 Z" fill="#2f7d1f"/>
    </svg>
    <div class="front-brand">
      <span class="brand-dot"></span>
      <span class="brand-name">Harbor Lane Realty Inc</span>
    </div>
    <div class="divider"></div>
    <div class="holder">
      <h1 class="holder-name">Dale Morrick</h1>
      <p class="holder-title">Managing Director</p>
    </div>
    <ul class="contact-list">
      <li><span class="icon"><svg viewBox="0 0 24 24"><path d="M6 3l3 0 1.5 5-2 1.5a11 11 0 0 0 6 6l1.5-2 5 1.5v3a2 2 0 0 1-2 2A17 17 0 0 1 4 5a2 2 0 0 1 2-2z" fill="#2f7d1f"/></svg></span>555-271-6094</li>
      <li><span class="icon"><svg viewBox="0 0 24 24"><rect x="3" y="6" width="18" height="12" rx="1.5" fill="#2f7d1f"/><path d="M3.5 7l8.5 6 8.5-6" stroke="#fff" stroke-width="1.6" fill="none"/></svg></span>dmorrick@mailbox.test</li>
      <li><span class="icon"><svg viewBox="0 0 24 24"><rect x="4" y="8" width="16" height="11" fill="#2f7d1f"/><path d="M4 8l4-4h8l4 4" fill="#1f5e14"/></svg></span>PO Box 718269</li>
      <li><span class="icon"><svg viewBox="0 0 24 24"><path d="M12 3l9 8h-3v9h-4v-6h-4v6H6v-9H3z" fill="#2f7d1f"/></svg></span>Cedar Marsh FL 32987</li>
    </ul>
  </section>

  <section class="card card-back" aria-label="Business card back">
    <svg class="card-bg" viewBox="0 0 700 400" preserveAspectRatio="none" aria-hidden="true">
      <defs>
        <radialGradient id="backGlow" cx="0.5" cy="0.4" r="0.55">
          <stop offset="0" stop-color="#4a4a4a"/>
          <stop offset="1" stop-color="#0c0c0c"/>
        </radialGradient>
        <linearGradient id="backGreen" x1="0" y1="0" x2="1" y2="0">
          <stop offset="0" stop-color="#2f7d1f"/>
          <stop offset="1" stop-color="#1f5e14"/>
        </linearGradient>
      </defs>
      <rect width="700" height="400" fill="url(#backGreen)"/>
      <path d="M180 400 C 60 250, 140 40, 320 0 L 470 0 C 620 60, 640 300, 520 400 Z" fill="#8fb43a"/>
      <path d="M196 400 C 82 250, 158 46, 326 0 L 462 0 C 604 66, 622 300, 506 400 Z" fill="url(#backGlow)"/>
    </svg>
    <div class="back-brand">
      <span class="brand-dot"></span>
      <span class="brand-name">Harbor Lane Realty Inc</span>
    </div>
    <p class="tagline">Buy Houses Cash</p>
    <div class="tagline-rule"></div>
  </section>

</body>
</html>
```